Create our new Brightcup Coffee Syrup Label designs. A delicious job!

Design a front label for a range of coffee syrup flavours. The brand is 'Brightcup Coffee Syrups'. The flavours, vanilla, hazelnut and caramel.
Our coffee syrups are made with only natural colours and flavours and are positioned in the popular premium space in Australian and international cafes.
The labels will be applied to 750 ml Boston Bottles (see attached image).
Given that coffee syrups are often positioned in high visibility locations in cafes, they can be considered as objects of functional beauty.
This range is a sub brand for our company and I have attached our main brand images in the flavours we want. we want this brand to look different to this Marlowe branded range, but included the image to show what we are currently doing in this space.
The different flavours can be identified by a combination of colour and text, which may be a line or section of the otherwise same overall design.
We are going to do a 2 part label with the front just carrying Brand and flavour descriptors plus 750 ml.
Total Bottle height is 240 mm bottle width is 70 mm

Target Market(s)

Cafe patrons, primarily women, 18-35, Middle class in terms of economics, regular cafe patrons. Who are looking for a guilt free treat in their busy day.

Logo Text

Brightcup Coffee Syrups Vanilla (or Hazelnut, or Caramel) 750 ml

Logo styles of interest
Pictorial/Combination Logo
Font styles to use
Sans Serif

Colors

Designer to choose colors to be used in the design.

Requirements
Must have
• A clear design, which is a combination of font and image. it needs to be legible from up to 2m away (across a counter in a cafe).
• We would like to see a device, which may be a gold drop, that may be the 'brightcup' meant to the coffee.
• The way our coffee syrups are used is by adding a small amount (15 ml) to a cup
• of coffee, this adds both flavour and sweetness to the overall coffee experience, and cafes charge a premium for this service. We want our package to show this will be a great thing to do.
• We have a few options in terms of Label stock. We can print on a foil, that will allow a metallic sheen to come through the colours (see example of the Marlowe branded bottles.
Nice to have
• We are looking for a modern, clean and distinctive look and feel to this range.
• I have added a key line for the front and back label, however we can create a different label die line should the design warrant that. Note this is just for the front label.
Should not have
• Difficult to read fonts or imagery that is not clear.
• Should look different to the Marlowe branded product range.

```html
<!DOCTYPE html>
<html lang="en">
<head>
<meta charset="utf-8">
<title>Brightcup Coffee Syrups – Hazelnut Front Label</title>
<link rel="stylesheet" href="https://fonts.googleapis.com/css2?family=Bebas+Neue&family=Kaushan+Script&family=Oswald:wght@600&display=swap">
<style>
  :root {
    --page-bg: #ffffff;
    --label-black: #0e0e0e;
    --label-charcoal: #3a3a3c;
    --gold: #c9a021;
    --gold-bright: #e2b92c;
    --ink-white: #ffffff;
  }
  html, body {
    margin: 0;
    padding: 0;
    width: 1200px;
    height: 1049px;
    overflow: hidden;
    background: var(--page-bg);
  }
  .label-canvas {
    display: block;
    width: 1200px;
    height: 1049px;
  }
  .label-frame { stroke: var(--gold); stroke-width: 24; stroke-linejoin: round; }
  .crest-ring { fill: none; stroke: var(--ink-white); stroke-width: 3.5; }
  .established {
    font-family: "Bebas Neue", sans-serif;
    font-size: 44px;
    fill: var(--ink-white);
    letter-spacing: 1px;
  }
  .brand-name {
    font-family: "Bebas Neue", sans-serif;
    font-size: 136px;
    fill: var(--gold-bright);
  }
  .product-line {
    font-family: "Bebas Neue", sans-serif;
    font-size: 66px;
    fill: var(--ink-white);
  }
  .flavour-rule { fill: var(--gold); }
  .flavour-name {
    font-family: "Kaushan Script", cursive;
    font-size: 108px;
    fill: var(--gold-bright);
  }
  .volume-info {
    font-family: "Oswald", sans-serif;
    font-weight: 600;
    font-size: 21px;
    letter-spacing: 7px;
    fill: var(--ink-white);
  }
  .volume-divider { fill: var(--ink-white); }
</style>
</head>
<body>
<svg class="label-canvas" viewBox="0 0 915 800" xmlns="http://www.w3.org/2000/svg" role="img" aria-label="Brightcup Coffee Syrups Hazelnut front label, 750 ml">
  <defs>
    <linearGradient id="labelFill" x1="0" y1="0" x2="1" y2="0">
      <stop offset="0" stop-color="var(--label-black)"/>
      <stop offset="0.55" stop-color="var(--label-charcoal)"/>
      <stop offset="1" stop-color="var(--label-black)"/>
    </linearGradient>
  </defs>

  <!-- Label body with gold frame -->
  <path class="label-frame" fill="url(#labelFill)"
        d="M202,773 V250 C202,178 298,128 393,121 A68,68 0 1 1 509,121 C604,128 701,178 701,250 V773 Z"/>

  <!-- Crest badge -->
  <circle class="crest-ring" cx="451" cy="86" r="60"/>

  <!-- Brand block -->
  <text class="established" x="451" y="233" text-anchor="middle">EST. 2018</text>
  <text class="brand-name" x="451" y="336" text-anchor="middle" textLength="420" lengthAdjust="spacingAndGlyphs">BRIGHTCUP</text>
  <text class="product-line" x="451" y="410" text-anchor="middle" textLength="316" lengthAdjust="spacingAndGlyphs">COFFEE SYRUPS</text>

  <!-- Flavour band -->
  <polygon class="flavour-rule" points="245,524 660,437 658,444 247,529"/>
  <text class="flavour-name" x="445" y="630" text-anchor="middle" transform="rotate(-11 445 600)">Hazelnut</text>
  <polygon class="flavour-rule" points="245,686 658,598 656,605 247,691"/>

  <!-- Volume -->
  <text class="volume-info" x="397" y="746" text-anchor="end">750 ML</text>
  <rect class="volume-divider" x="404" y="717" width="4" height="33"/>
  <text class="volume-info" x="432" y="746">15 ML / CUP</text>
</svg>
</body>
</html>
```